New Business Cards for Torvin Group

We need a new Business Card to compliment our new logo. We are a vibrant design, manufacture and install business providing recreation areas, public parks and Municipal spaces. We want business cards that are classy, modern and clean.

We have recently changed our logo, and are celebrating our 40th anniversary. We want business cards with a new modern design to reflect our status.

Target Market(s)

Customers

Contact Information for Business Card

We need all the details of our 3 offices as per the business card attached. Please disregard the old logo on the business card, the other three files show our new logo.

Requirements
Must have
• All info as per attached business card but with new logo.
Nice to have

```html
<!DOCTYPE html>
<html lang="en">
<head>
<meta charset="utf-8">
<title>Torvin Group – Business Card</title>
<link rel="stylesheet" href="https://fonts.googleapis.com/css2?family=Lato:wght@300;400;700;900&display=swap">
<style>
  :root {
    --brand-red: #e3000f;
    --ink: #1f1f1f;
    --ink-soft: #4a4a4a;
    --logo-grey: #3d3e42;
    --paper: #ffffff;
    --backdrop: #e4e4e4;
  }
  * { box-sizing: border-box; margin: 0; padding: 0; }
  html, body { width: 1200px; height: 900px; overflow: hidden; }
  body {
    background: var(--backdrop);
    font-family: "Lato", sans-serif;
    color: var(--ink);
    position: relative;
  }
  .card {
    position: absolute;
    left: 100px; top: 165px;
    width: 1000px; height: 570px;
    background: var(--paper);
    overflow: hidden;
  }
  .person { position: absolute; left: 32px; top: 48px; }
  .person__name {
    font-weight: 700; font-size: 40px; line-height: 1;
    color: var(--brand-red); letter-spacing: -0.3px;
  }
  .person__title {
    font-weight: 300; font-size: 31px; line-height: 1.2;
    color: var(--ink-soft); margin-top: 4px;
  }
  .person__contacts { margin-top: 14px; }
  .contact-line {
    display: flex; align-items: center; gap: 12px;
    font-weight: 300; font-size: 23px; color: var(--ink-soft);
    height: 37px;
  }
  .icon { flex: none; width: 30px; height: 30px; }
  .icon--small { width: 26px; height: 26px; }

  .brand {
    position: absolute; left: 560px; top: 110px;
    display: flex; align-items: center; gap: 18px;
  }
  .brand__mark {
    width: 70px; height: 70px; border-radius: 50%;
    background: var(--brand-red);
  }
  .brand__name {
    font-weight: 900; font-size: 52px; line-height: 1;
    color: var(--logo-grey); letter-spacing: 0.5px;
  }

  .office { position: absolute; top: 315px; width: 285px; }
  .office--head { left: 33px; }
  .office--dubai { left: 361px; }
  .office--qatar { left: 689px; }
  .office__heading {
    text-align: center; font-weight: 700; font-size: 27px;
    color: var(--brand-red); height: 36px; line-height: 36px;
  }
  .office__box {
    margin-top: 4px; height: 240px;
    border: 1.5px solid var(--brand-red); border-bottom: none;
    border-radius: 14px 14px 0 0;
    padding: 12px 14px 0 16px;
  }
  .office__line {
    display: flex; align-items: center; gap: 9px;
    font-size: 19px; font-weight: 400; color: var(--ink);
    height: 41px; white-space: nowrap;
  }

  .footer-band {
    position: absolute; left: 0; right: 0; bottom: 0; height: 28px;
    background: var(--brand-red);
  }
  .footer-pill {
    position: absolute; left: 212px; width: 565px; bottom: -20px; height: 62px;
    background: var(--brand-red);
    border: 4px solid var(--paper);
    border-radius: 24px;
    display: flex; justify-content: center; padding-top: 4px;
    font-weight: 300; font-size: 25px; color: var(--paper);
    letter-spacing: 0.3px;
  }
</style>
</head>
<body>
<svg width="0" height="0" style="position:absolute" aria-hidden="true">
  <defs>
    <symbol id="icon-phone" viewBox="0 0 30 30">
      <circle cx="15" cy="15" r="13.5" fill="none" stroke="#e3000f" stroke-width="2"/>
      <path d="M10.5 8.5c.8-.6 1.6-.5 2 .2l1.3 2.3c.3.6.1 1.2-.4 1.6l-.9.6c.7 1.9 2.3 3.5 4.2 4.3l.6-.9c.4-.5 1-.7 1.6-.4l2.3 1.3c.7.4.8 1.2.2 2l-1 1.2c-.7.8-2 .9-3.4.3-3.3-1.4-6-4.1-7.4-7.4-.6-1.4-.5-2.7.3-3.4z" fill="#333"/>
    </symbol>
    <symbol id="icon-mail" viewBox="0 0 30 30">
      <circle cx="15" cy="15" r="13.5" fill="none" stroke="#e3000f" stroke-width="2"/>
      <rect x="8" y="10.5" width="14" height="9.5" rx="1" fill="#222"/>
      <path d="M8.5 11l6.5 5 6.5-5M8.5 19.5l4.8-4.2M21.5 19.5l-4.8-4.2" fill="none" stroke="#fff" stroke-width="1.1"/>
    </symbol>
    <symbol id="icon-building" viewBox="0 0 30 30">
      <circle cx="15" cy="15" r="13.5" fill="none" stroke="#e3000f" stroke-width="2"/>
      <rect x="8.5" y="8.5" width="13" height="13" fill="none" stroke="#555" stroke-width="1.3"/>
      <path d="M8.5 12h13M11 14.5h2v2h-2zM14 14.5h2v2h-2zM17 14.5h2v2h-2zM13.5 21.5v-3h3v3" fill="none" stroke="#555" stroke-width="1"/>
    </symbol>
    <symbol id="icon-landline" viewBox="0 0 30 30">
      <circle cx="15" cy="15" r="13.5" fill="none" stroke="#e3000f" stroke-width="2"/>
      <path d="M8 12.5c0-2 3.2-3.5 7-3.5s7 1.5 7 3.5v1h-3v-1.5h-8v1.5H8z" fill="#222"/>
      <path d="M10.5 14.5h9l1.5 6.5H9z" fill="#222"/>
      <circle cx="15" cy="17.5" r="1.6" fill="#fff"/>
    </symbol>
    <symbol id="icon-fax" viewBox="0 0 30 30">
      <circle cx="15" cy="15" r="13.5" fill="none" stroke="#e3000f" stroke-width="2"/>
      <rect x="11" y="8" width="8" height="5" fill="none" stroke="#666" stroke-width="1.2"/>
      <rect x="8.5" y="13" width="13" height="7.5" rx="1" fill="none" stroke="#666" stroke-width="1.3"/>
      <path d="M11 16h8M11 18h5" stroke="#666" stroke-width="1"/>
    </symbol>
  </defs>
</svg>

<main class="card">
  <section class="person">
    <h1 class="person__name">Marek Lindqvist</h1>
    <p class="person__title">Managing Partner</p>
    <div class="person__contacts">
      <p class="contact-line"><svg class="icon"><use href="#icon-phone"/></svg>+971(0)50 7348120</p>
      <p class="contact-line"><svg class="icon"><use href="#icon-mail"/></svg>marek@torvingroup.com</p>
    </div>
  </section>

  <div class="brand">
    <span class="brand__mark"></span>
    <span class="brand__name">TORVIN GROUP</span>
  </div>

  <section class="office office--head">
    <h2 class="office__heading">Head Office</h2>
    <div class="office__box">
      <p class="office__line"><svg class="icon icon--small"><use href="#icon-building"/></svg>31842 Abu Dhabi, U.A.E</p>
      <p class="office__line"><svg class="icon icon--small"><use href="#icon-landline"/></svg>+971(0)2 5830417</p>
      <p class="office__line"><svg class="icon icon--small"><use href="#icon-fax"/></svg>+971(0)2 5830418</p>
      <p class="office__line"><svg class="icon icon--small"><use href="#icon-mail"/></svg>sales@torvingroup.com</p>
    </div>
  </section>

  <section class="office office--dubai">
    <h2 class="office__heading">Dubai Office</h2>
    <div class="office__box">
      <p class="office__line"><svg class="icon icon--small"><use href="#icon-building"/></svg>517264 Abu Dhabi, U.A.E</p>
      <p class="office__line"><svg class="icon icon--small"><use href="#icon-landline"/></svg>+971(0)4 6072385</p>
      <p class="office__line"><svg class="icon icon--small"><use href="#icon-fax"/></svg>+971(0)2 6072390</p>
      <p class="office__line"><svg class="icon icon--small"><use href="#icon-mail"/></svg>sales@torvingroup.com</p>
    </div>
  </section>

  <section class="office office--qatar">
    <h2 class="office__heading">Qatar Office</h2>
    <div class="office__box">
      <p class="office__line"><svg class="icon icon--small"><use href="#icon-building"/></svg>27093 Doha, Qatar</p>
      <p class="office__line"><svg class="icon icon--small"><use href="#icon-landline"/></svg>+974(0)2 55817342</p>
      <p class="office__line"><svg class="icon icon--small"><use href="#icon-fax"/></svg>+971(0)2 55917408</p>
      <p class="office__line"><svg class="icon icon--small"><use href="#icon-mail"/></svg>sales@torvingroup.com</p>
    </div>
  </section>

  <div class="footer-band"></div>
  <div class="footer-pill">www.torvingroup.com</div>
</main>
</body>
</html>
```